Website Banners

I am working on a new website and need some banners for the main service pages. I will need 5 in total and may potentially choose from multi-designers and increase the payment or will choose the designer for all 5 based on the first one.

I am including a s the link to the development site. all the graphics in there at the moment are conceptual but give you an idea of what I am looking for.

___________________________

http://dev.morvelquist.example:8080/

On the home page I am looking for the main banner to represent an organisation moving or transitioning to the cloud but I want to use an individual (like a runner) to represent that.

I would like a text overlay for that banner to say: "Businesses don't transition themselves, so what are you waiting for?" or "Get ready for business at the speed of sound"

http://dev.morvelquist.example:8080/about-2/

On the About page I am looking for two banners. The first one to depict an Australian city street with a text overlay to say: "We stand for mid-market Australia". The second one to depict a local government/council image with a text overlay to say "We are local government and public sector experts"

http://dev.morvelquist.example:8080/about-2

On the Advisory page I am looking for a banner that depicts "trust" in a professional business sense with a text overlay to say "Challenge yourself - or have us do it for you"

http://dev.morvelquist.example:8080/consulting/

On the Consulting page I am looking for two banners. The first one to depict "getting your hands dirty" or "getting in there and getting the job done" with a text overlay to say "If you want success in your business put us there". The second one with an image to depict a competitive consulting environment with a text overlay to say "We understand we are an option but our approach is to make you a priority"

5 all up. I don't care which one you respond to.

My logo is attached.

I have also attached a couple of other designs that I have gone for in the past.

Target Market(s)

mid market (sized) businesses

Industry/Entity Type

It Service

Font styles to use
Serif

Colors
33a6d7
3176b4
f68d4d
f37122
ffffff

Requirements
Must have
• energy

```html
<!DOCTYPE html>
<html lang="en">
<head>
<meta charset="utf-8">
<title>Halvern Ridge Advisory – Transition Banner</title>
<link rel="stylesheet" href="https://fonts.googleapis.com/css2?family=Oswald:wght@400;500&display=swap">
<style>
  :root {
    --page-bg: #ececec;
    --brand-orange: #f37122;
    --brand-blue: #3176b4;
    --brand-navy: #2b4c9e;
    --text-light: #ffffff;
    --sky-top: #2f7fc4;
    --sky-mid: #a9cbe6;
    --haze: #d9e6ee;
    --ridge: #5d7452;
    --rock: #8f6d4c;
    --foreground: #b58a62;
  }
  * { margin: 0; padding: 0; box-sizing: border-box; }
  html, body {
    width: 1200px;
    height: 590px;
    overflow: hidden;
    background: var(--page-bg);
  }
  .banner {
    position: absolute;
    left: 20px;
    top: 53px;
    width: 1160px;
    height: 483px;
    overflow: hidden;
    font-family: "Oswald", "Arial Narrow", sans-serif;
  }
  .banner__scene {
    position: absolute;
    inset: 0;
    background:
      radial-gradient(ellipse 70% 30% at 60% 100%, var(--foreground) 0%, rgba(181,138,98,0) 70%),
      linear-gradient(180deg,
        var(--sky-top) 0%,
        var(--sky-mid) 28%,
        var(--haze) 46%,
        var(--ridge) 62%,
        var(--ridge) 74%,
        var(--rock) 90%,
        var(--foreground) 100%);
  }
  .brand {
    position: absolute;
    left: 196px;
    top: 78px;
    color: var(--brand-navy);
    font-weight: 500;
    font-size: 40px;
    letter-spacing: 1px;
    text-transform: uppercase;
    line-height: 1;
  }
  .headline {
    position: absolute;
    display: flex;
    align-items: center;
    justify-content: center;
    color: var(--text-light);
    font-weight: 400;
    font-size: 39px;
    text-transform: uppercase;
    line-height: 1;
    white-space: nowrap;
    box-shadow: 0 2px 6px rgba(0,0,0,0.25);
  }
  .headline--lead {
    left: 51px;
    top: 187px;
    width: 679px;
    height: 75px;
    background: var(--brand-orange);
  }
  .headline--question {
    left: 72px;
    top: 267px;
    width: 628px;
    height: 83px;
    background: var(--brand-blue);
  }
</style>
</head>
<body>
  <section class="banner">
    <div class="banner__scene" role="img" aria-label="Runner celebrating with a raised fist on a rocky mountain summit above a valley under a blue sky with clouds"></div>
    <div class="brand">Halvern Ridge Advisory</div>
    <h1 class="headline headline--lead">Businesses don't transition themselves</h1>
    <p class="headline headline--question">So what are you waiting for?</p>
  </section>
</body>
</html>
```